今回はコーポレートサイトのTOPページのデザインをお願いしたく思います。

【素材】
素材に関しては、ロゴや写真等は現在準備中でして、
デザインの際は仮のオブジェクトを入れて対応して頂ければと思います。

【サイト構成】
サイトの構成については、ラフを書きましたので下記URLからダウンロードお願いします。
http://qvn.jp/PbLwoR

※PCを想定したデザインでお願いいたします。

【イメージ】
以下が現在の「アオバエステート株式会社」のコーポレートサイトになります。
http://www.aoba-estate.co.jp/

今回ご提案いただく新しいサイトのデザインは上記のものから一新して

1.スタイリッシュ
2.NY
3.最先端
4.近未来
5.エネルギッシュ
6.エキサイティング
7.自由
8.それでいてシンプル

なイメージ、従来の不動産会社のイメージに囚われないものにしたく思います。

【参考サイト】
https://www.kumonomi.co.jp/

1ページ
グレー系
今回のデザインで採用させて頂いた方には、
コーポレートサイトの「代表メッセージ」「ニュース」「投資実績」の他3ページのデザインやコーディングなど、他のお仕事に関してもご相談させて頂ければと思います。
(もちろん当案件のみご希望の方からも募集しており、採用有無には関係ありません。)

色のコンセプトと対応の早さ、デザインの良さで決定致しました。

皆さま、お忙しい所多くのご提案を頂きまして誠にありがとうございます。
また何かございましたらお願いをさせて頂きますので引き続き宜しくお願い致します。

```html
<!DOCTYPE html>
<html lang="ja">
<head>
<meta charset="utf-8">
<title>AOBA | 不動産の新しい未来をつくる</title>
<link rel="stylesheet" href="https://fonts.googleapis.com/css2?family=Oswald:wght@300;400;500&family=Noto+Sans+JP:wght@300;400;500;700&display=swap">
<style>
:root{
  --ink:#111214;
  --night:#17191c;
  --works:#2b2c2f;
  --panel:#222326;
  --panel-soft:#35363a;
  --line:#8a8b8e;
  --white:#ffffff;
  --paper:#ffffff;
  --text:#333333;
  --muted:#9a9b9e;
  --accent:#e0463a;
  --label-bg:#f0f0f0;
}
*{margin:0;padding:0;box-sizing:border-box}
html,body{width:1200px;height:3924px;overflow:hidden}
body{background:var(--ink);color:var(--white);font-family:"Noto Sans JP",sans-serif;position:relative}
.en{font-family:"Oswald",sans-serif}

/* header + hero */
.hero{position:absolute;left:0;top:0;width:1200px;height:740px;
  background:radial-gradient(ellipse at 45% 62%,#3c4450 0%,#1c2129 45%,#0b0d11 100%)}
.site-header{position:absolute;left:0;top:0;width:1200px;height:60px;display:flex;align-items:center;justify-content:space-between;padding:0 20px}
.brand{font-family:"Oswald",sans-serif;font-weight:400;font-size:20px;letter-spacing:4px}
.global-nav{display:flex;gap:36px;font-family:"Oswald",sans-serif;font-size:13px;letter-spacing:2px;margin-right:24px}
.global-nav a{color:var(--white);text-decoration:none}
.hero-title{position:absolute;left:0;width:1200px;top:305px;text-align:center;font-family:"Oswald",sans-serif;font-weight:300;font-size:118px;letter-spacing:34px;text-indent:34px}
.scroll{position:absolute;left:599px;top:640px;width:1px;height:70px;background:rgba(255,255,255,.6)}
.scroll-label{position:absolute;left:0;width:1200px;top:690px;text-align:center;font-family:"Oswald",sans-serif;font-size:10px;letter-spacing:2px;color:rgba(255,255,255,.6)}

/* philosophy */
.philosophy{position:absolute;left:0;top:740px;width:1200px;height:320px;background:var(--ink);text-align:center}
.section-title{font-family:"Oswald",sans-serif;font-weight:400;font-size:26px;letter-spacing:6px}
.section-title::after{content:"";display:block;width:2px;height:22px;background:currentColor;margin:14px auto 0}
.philosophy .section-title{position:absolute;top:98px;width:100%}
.philosophy-lead{position:absolute;top:176px;width:100%;font-size:44px;font-weight:400;letter-spacing:10px}

/* works */
.works{position:absolute;left:0;top:1060px;width:1200px;height:1520px;background:var(--works)}
.works .section-title{position:absolute;top:96px;width:100%;text-align:center}
.works-row{position:absolute;left:0;width:1200px;height:360px}
.edge{position:absolute;top:0;height:360px;width:132px;background:linear-gradient(180deg,#3a3b3f,#26272a)}
.edge.left{left:0}.edge.right{left:1068px}
.photo{position:absolute;top:0;width:468px;height:360px}
.work-info{position:absolute;top:0;width:468px;height:360px;background:linear-gradient(135deg,#2e2f33,#1c1d20);overflow:hidden}
.work-num{position:absolute;right:14px;top:12px;font-family:"Oswald",sans-serif;font-size:118px;font-weight:400;color:rgba(255,255,255,.1);line-height:1}
.work-meta{position:absolute;left:36px;top:82px;font-family:"Oswald",sans-serif;font-size:11px;letter-spacing:1px;display:flex;gap:8px;align-items:center}
.tag{background:var(--white);color:var(--ink);font-family:"Noto Sans JP",sans-serif;font-size:10px;padding:1px 6px}
.work-title{position:absolute;left:36px;top:108px;font-size:20px;font-weight:500;letter-spacing:1px}
.work-text{position:absolute;left:36px;top:148px;width:380px;font-size:12px;line-height:1.9;color:#c8c9cb}
.view-more{position:absolute;right:24px;bottom:24px;display:flex;align-items:center;gap:10px;font-family:"Oswald",sans-serif;font-size:11px;letter-spacing:1px}
.view-more svg{display:block}
.all-works{position:absolute;left:468px;top:1368px;width:264px;height:56px;border:1px solid var(--white);display:flex;align-items:center;justify-content:center;font-family:"Oswald",sans-serif;font-size:17px;letter-spacing:3px}

/* profile */
.profile{position:absolute;left:0;top:2580px;width:1200px;height:600px;background:var(--paper);color:var(--text)}
.profile .section-title{position:absolute;top:58px;width:100%;text-align:center;color:var(--ink)}
.profile-table{position:absolute;top:160px;border-collapse:collapse;font-size:12px}
.profile-table th{width:100px;background:var(--label-bg);font-weight:500;text-align:left;padding:12px 16px;border-bottom:1px solid #ddd;vertical-align:top}
.profile-table td{padding:12px 16px;border-bottom:1px solid #ddd;line-height:1.7;vertical-align:top}
.profile-table.left{left:148px;width:432px}
.profile-table.right{left:612px;width:436px}

/* map */
.map{position:absolute;left:0;top:3180px;width:1200px;height:348px;background:linear-gradient(135deg,#2c2d30,#1e1f22 60%,#26272a)}
.map-pin{position:absolute;left:588px;top:94px}

/* footer */
.site-footer{position:absolute;left:0;top:3528px;width:1200px;height:396px;background:var(--night);text-align:center}
.footer-brand{position:absolute;top:54px;width:100%;font-family:"Oswald",sans-serif;font-size:34px;letter-spacing:10px;text-indent:10px}
.footer-address{position:absolute;top:112px;width:100%;font-size:12px;line-height:1.8;color:#d0d0d0}
.footer-nav{position:absolute;top:214px;width:100%;display:flex;justify-content:center;gap:40px;font-family:"Oswald",sans-serif;font-size:13px;letter-spacing:2px}
.copyright{position:absolute;left:0;bottom:0;width:100%;height:64px;background:#0c0d0f;display:flex;align-items:center;justify-content:center;font-size:10px;color:var(--muted);letter-spacing:.5px}
</style>
</head>
<body>

<section class="hero" role="img" aria-label="夜景の高層ビル群を見下ろす都市の空撮写真">
  <header class="site-header">
    <div class="brand">AOBA</div>
    <nav class="global-nav"><a>TOP</a><a>ABOUT</a><a>WORKS</a><a>NEWS</a><a>CONTACT</a></nav>
  </header>
  <h1 class="hero-title">AOBA</h1>
  <div class="scroll-label">SCROLL</div>
  <div class="scroll"></div>
</section>

<section class="philosophy">
  <h2 class="section-title">PHILOSOPHY</h2>
  <p class="philosophy-lead">不動産の新しい未来をつくる</p>
</section>

<section class="works">
  <h2 class="section-title">WORKS</h2>

  <div class="works-row" style="top:212px">
    <div class="edge left"></div>
    <div class="photo" style="left:132px;background:linear-gradient(180deg,#9fb3c9 0%,#e4e6e8 45%,#8e8f91 100%)" role="img" aria-label="白いモダンな二階建て住宅の外観写真"></div>
    <article class="work-info" style="left:600px">
      <div class="work-num">01</div>
      <div class="work-meta">WORKS 01 <span class="tag">新築</span></div>
      <h3 class="work-title">深谷市H様邸</h3>
      <p class="work-text">住まいづくりを通じて「家族の時間」を大切にし、暮らしやすさと上質さを両立した住まいをご提案いたしました。外観から内装まで細部にこだわった一邸です。</p>
      <div class="view-more">VIEW MORE <svg width="28" height="28" viewBox="0 0 28 28"><circle cx="14" cy="14" r="14" fill="#fff"/><path d="M11 9l5 5-5 5" stroke="#222" stroke-width="2" fill="none"/></svg></div>
    </article>
    <div class="edge right"></div>
  </div>

  <div class="works-row" style="top:572px">
    <div class="edge left"></div>
    <article class="work-info" style="left:132px">
      <div class="work-num">02</div>
      <div class="work-meta">WORKS 02 <span class="tag">新築</span></div>
      <h3 class="work-title">大型収納の家</h3>
      <p class="work-text">住まいづくりを通じて「家族の時間」を大切にし、収納量と動線にこだわった住まいをご提案いたしました。すっきり暮らせるプランの一邸です。</p>
      <div class="view-more">VIEW MORE <svg width="28" height="28" viewBox="0 0 28 28"><circle cx="14" cy="14" r="14" fill="#fff"/><path d="M11 9l5 5-5 5" stroke="#222" stroke-width="2" fill="none"/></svg></div>
    </article>
    <div class="photo" style="left:600px;background:linear-gradient(180deg,#b7cde3 0%,#ead9c3 50%,#b9a58c 100%)" role="img" aria-label="ベージュ外壁の二階建て住宅の外観写真"></div>
    <div class="edge right"></div>
  </div>

  <div class="works-row" style="top:932px">
    <div class="edge left"></div>
    <div class="photo" style="left:132px;background:linear-gradient(180deg,#a9c2de 0%,#d9d6cf 50%,#6e6a62 100%)" role="img" aria-label="平屋建て住宅の外観写真"></div>
    <article class="work-info" style="left:600px">
      <div class="work-num">03</div>
      <div class="work-meta">WORKS 03 <span class="tag">新築</span></div>
      <h3 class="work-title">深谷市上柴町N様邸</h3>
      <p class="work-text">住まいづくりを通じて「家族の時間」を大切にし、ゆとりある平屋の住まいをご提案いたしました。庭とつながる開放的な一邸です。</p>
      <div class="view-more">VIEW MORE <svg width="28" height="28" viewBox="0 0 28 28"><circle cx="14" cy="14" r="14" fill="#fff"/><path d="M11 9l5 5-5 5" stroke="#222" stroke-width="2" fill="none"/></svg></div>
    </article>
    <div class="edge right"></div>
  </div>

  <a class="all-works">ALL WORKS</a>
</section>

<section class="profile">
  <h2 class="section-title">PROFILE</h2>
  <table class="profile-table left">
    <tr><th>社名</th><td>アオバエステート株式会社</td></tr>
    <tr><th>所在地</th><td>〒150-0002 東京都渋谷区渋谷3-11-8<br>ミドリテラス渋谷5F</td></tr>
    <tr><th>代表</th><td>青葉 健一</td></tr>
    <tr><th>設立</th><td>昭和55年2月1日</td></tr>
    <tr><th>資本金</th><td>5,000万円</td></tr>
    <tr><th>免許</th><td>宅建業者免許番号　東京都知事（1）第00000号<br>不動産特定共同事業</td></tr>
  </table>
  <table class="profile-table right">
    <tr><th>従業員数</th><td>8名</td></tr>
    <tr><th>加盟団体</th><td>全国宅地建物取引業協会<br>不動産流通協会</td></tr>
    <tr><th>取引銀行</th><td>みなと信用銀行<br>ひかり中央銀行<br>武蔵野中央銀行</td></tr>
    <tr><th>業務内容</th><td>不動産売買仲介事業<br>賃貸管理事業<br>一般建築<br>宅地造成工事事業<br>土地建物売買事業<br>不動産投資事業</td></tr>
  </table>
</section>

<section class="map" role="img" aria-label="所在地周辺のダークトーンの地図">
  <svg class="map-pin" width="24" height="34" viewBox="0 0 24 34"><path d="M12 0C5.4 0 0 5.2 0 11.7 0 20 12 34 12 34s12-14 12-22.3C24 5.2 18.6 0 12 0z" fill="var(--accent)"/><circle cx="12" cy="11.5" r="4.5" fill="#fff"/></svg>
</section>

<footer class="site-footer">
  <div class="footer-brand">AOBA</div>
  <p class="footer-address">〒150-0002 東京都渋谷区渋谷3-11-8<br>ミドリテラス渋谷5F</p>
  <nav class="footer-nav"><a>TOP</a><a>ABOUT</a><a>WORKS</a><a>NEWS</a><a>CONTACT</a></nav>
  <div class="copyright">Copyright © 2017 AOBA Estate Inc. All Rights Reserved.</div>
</footer>

</body>
</html>
```